Business card design needed

the business is HR Consulting, but its for SME businesses who cant afford a permanent HR person. We sell an HR info system to help them meet minimum employment legislation but with this hope they then require us on a monthly subscription to phone or email us for HR advice. We are HR qualified mums working from home

So we will be partners to HR and Payroll systems known as kindle HR and Pluto

Target Market(s)

Small to medium businesses so not black and overly corporate, but having said that many are accounting businesses

Industry/Entity Type

Business

Contact Information for Business Card

Name of the company: Tandem HR

Me:Marta Kovalenko
Title:Managing Director

m: 0437 215 683
e: marta@tandemhr.com.au
w: www.tandemhr.com.au

What we do: HR Consulting, HR Systems and support, Payroll Advice

Requirements
Nice to have
• there is a company already out there known as Quartz professionals. I like the leaves at the end as I wanted something different like this to the usual business logos but still professional. I wanted a symbol to show calm, positive, ease flow going up ,etc. but realise they have the leaves and possibly cant copy, or can we?..( kite??, something calm and positive)dont know!!. Green and blue needed to be in it as nature and calm as well. I love the colours of www.stafflanefund.com ( attached the colours), as well as the calm wave line underneath. have a look as while they use green and blue I loved the purple colour thrown in there.Green and blue on their own are so overused. I want vibrant. I want double sided and when on a table I want it to stand out so maybe the purple colour (as per the colours on the fund website) solid on one side with just the 3 services we provide and personal and company name on front but need some creativity from you guys.

```html
<!DOCTYPE html>
<html lang="en">
<head>
<meta charset="utf-8">
<title>Tandem HR — Business Card</title>
<link rel="stylesheet" href="https://fonts.googleapis.com/css2?family=PT+Serif:wght@400;700&display=swap">
<style>
  :root {
    --page-bg: #ecebe6;
    --lime-light: #d2ea8a;
    --lime: #b5d83c;
    --lime-deep: #9cc42a;
    --lime-glow: rgba(230, 245, 170, 0.55);
    --ink: #3c3a3f;
    --white: #ffffff;
    --card-shadow: rgba(0, 0, 0, 0.28);
  }
  * { box-sizing: border-box; margin: 0; padding: 0; }
  html, body {
    width: 1200px;
    height: 1000px;
    overflow: hidden;
  }
  body {
    background: var(--page-bg);
    font-family: "PT Serif", Georgia, serif;
    position: relative;
  }
  .card {
    position: absolute;
    left: 260px;
    width: 680px;
    height: 390px;
    overflow: hidden;
    background: radial-gradient(ellipse 70% 80% at 52% 42%, var(--lime-light) 0%, var(--lime) 62%, var(--lime-deep) 100%);
    box-shadow: 0 6px 18px var(--card-shadow);
  }
  .card--front { top: 60px; }
  .card--back { top: 550px; }

  .card__pattern {
    position: absolute;
    border-radius: 40px;
    background: radial-gradient(ellipse at center, var(--lime-glow) 0%, rgba(230, 245, 170, 0.25) 55%, rgba(230, 245, 170, 0) 100%);
  }
  .card--front .card__pattern { left: 110px; top: 20px; width: 500px; height: 300px; }
  .card--back .card__pattern { left: 10px; top: 90px; width: 300px; height: 230px; }

  .card__waves {
    position: absolute;
    left: 0;
    bottom: 0;
    width: 680px;
    height: 80px;
  }
  .wordmark {
    position: absolute;
    font-weight: 700;
    color: var(--white);
    letter-spacing: 1px;
    line-height: 1;
    white-space: nowrap;
  }
  .card--front .wordmark { left: 60px; top: 90px; font-size: 66px; }
  .card--back .wordmark { left: 30px; top: 42px; font-size: 54px; }

  .services {
    position: absolute;
    left: 44px;
    top: 280px;
    font-size: 23px;
    line-height: 30px;
    color: var(--ink);
    text-shadow: 0 0 3px rgba(255, 255, 255, 0.8);
    white-space: nowrap;
  }

  .contact {
    position: absolute;
    left: 334px;
    top: 142px;
    padding-left: 14px;
    border-left: 2px solid var(--white);
    list-style: none;
    font-size: 25px;
    line-height: 36px;
    color: var(--ink);
    text-shadow: 0 0 3px rgba(255, 255, 255, 0.85);
    white-space: nowrap;
  }
  .contact__name,
  .contact__title {
    color: var(--white);
    text-shadow: 0 1px 2px rgba(40, 60, 0, 0.55);
  }
</style>
</head>
<body>

  <section class="card card--front" aria-label="Card front">
    <div class="card__pattern" role="img" aria-label="Soft pattern of floating translucent squares"></div>
    <svg class="card__waves" viewBox="0 0 680 80" aria-hidden="true">
      <path d="M0 60 C 180 40, 420 30, 680 10" fill="none" stroke="rgba(255,255,255,0.55)" stroke-width="3"/>
      <path d="M0 70 C 200 52, 430 44, 680 24" fill="none" stroke="rgba(255,255,255,0.35)" stroke-width="6"/>
      <path d="M0 79 C 220 64, 450 58, 680 40" fill="none" stroke="rgba(255,255,255,0.5)" stroke-width="2"/>
    </svg>
    <div class="wordmark">Tandem HR</div>
    <p class="services">HR Consulting, HR Systems and support, Payroll Advice</p>
  </section>

  <section class="card card--back" aria-label="Card back">
    <div class="card__pattern" role="img" aria-label="Soft pattern of floating translucent squares"></div>
    <svg class="card__waves" viewBox="0 0 680 80" aria-hidden="true">
      <path d="M0 20 C 200 26, 420 40, 680 36" fill="none" stroke="rgba(255,255,255,0.55)" stroke-width="3"/>
      <path d="M0 36 C 220 42, 440 56, 680 52" fill="none" stroke="rgba(255,255,255,0.35)" stroke-width="7"/>
      <path d="M0 52 C 230 56, 450 70, 680 68" fill="none" stroke="rgba(255,255,255,0.5)" stroke-width="2"/>
    </svg>
    <div class="wordmark">Tandem HR</div>
    <ul class="contact">
      <li class="contact__name">Marta Kovalenko</li>
      <li class="contact__title">Managing Director</li>
      <li class="contact__phone">0437 215 683</li>
      <li class="contact__email">marta@tandemhr.com.au</li>
      <li class="contact__web">www.tandemhr.com.au</li>
    </ul>
  </section>

</body>
</html>
```